Seven Quiet Rooms Poster

Seven Quiet Rooms is reaching out to designers, creatives and fans alike to help create an exciting new poster for the film as part of our Fundvaro campaign.

Seven Quiet Rooms is a multi-protagonist, multicultural, humanist drama inspired by the 2008 Mumbai terrorist attacks. Centering on a group of international tourists trapped in their hotel by Islamic fundamentalists, the film aims to explore the key issues facing our society, concerning atheism, religion, religious extremism and humanism.

The film’s poster will be a critical part of a film’s publicity and marketing portfolio and an important resource for the film to take into our festival campaign and distribution talks. We’re looking for a highly polished design that accurately represents the film and matches the standard of the finished film.

We will be uploading some of the best entries to our Chatterbox page for fans to vote on. If you do not wish for your design to appear on the page, please contact us.

You can find our teaser trailer on the Fundvaro link below. We’ve also provided some reference images (found here: http://lnk.example-short.net/Rk4WpZ) and also stills from the film to provide inspiration (found here: http://lnk.example-short.net/Tm8QvB) - how or if you use them is up to you.

Good luck and get designing!

http://www.fundvaro-example.com/projects/seven-quiet-rooms

Please note: Amber Tide Pictures reserves the right to select all promotional material for theatrical release.

Requirements
Must have
• Size: 27" x 40"
Should not have
• Please do not include the credit block on your designs.

```html
<!DOCTYPE html>
<html lang="en">
<head>
<meta charset="utf-8">
<title>Seven Quiet Rooms — Poster</title>
<link rel="stylesheet" href="https://fonts.googleapis.com/css2?family=Poppins:wght@300;700&display=swap">
<style>
  :root {
    --paper: #ffffff;
    --title-red: #ee1c24;
    --blood-dark: #4e090c;
    --blood-mid: #8a1016;
    --steel-light: #a59e94;
    --steel-mid: #6e6861;
    --steel-dark: #231f1c;
  }
  html, body {
    margin: 0;
    padding: 0;
    overflow: hidden;
    background: var(--paper);
  }
  .poster {
    position: relative;
    width: 810px;
    height: 1200px;
    background: var(--paper);
    overflow: hidden;
  }
  .blood-splatter {
    position: absolute;
    left: 520px;
    top: 100px;
    width: 170px;
    height: 190px;
    border-radius: 46% 54% 50% 50% / 55% 45% 55% 45%;
    background: radial-gradient(ellipse at 50% 55%, var(--blood-dark) 0%, var(--blood-mid) 55%, rgba(138, 16, 22, 0) 74%);
  }
  .title {
    position: absolute;
    left: 0;
    top: 178px;
    width: 810px;
    margin: 0;
    text-align: center;
    white-space: nowrap;
    font-family: "Poppins", sans-serif;
    font-size: 76px;
    line-height: 90px;
    letter-spacing: -1px;
    color: var(--title-red);
  }
  .title-light { font-weight: 300; }
  .title-bold { font-weight: 700; }
  .rifle-crowd {
    position: absolute;
    left: 0;
    top: 756px;
    width: 810px;
    height: 444px;
    display: block;
  }
</style>
</head>
<body>
  <main class="poster">
    <div class="blood-splatter" role="img" aria-label="Dark red blood splatter behind the title"></div>
    <h1 class="title"><span class="title-light">SEVEN QUIET </span><span class="title-bold">ROOMS</span></h1>
    <svg class="rifle-crowd" viewBox="0 756 810 444" role="img" aria-label="A crowd of upright assault rifles rising from the bottom edge">
      <defs>
        <linearGradient id="steel" x1="0" y1="756" x2="0" y2="1200" gradientUnits="userSpaceOnUse">
          <stop offset="0" stop-color="var(--steel-light)"/>
          <stop offset="0.5" stop-color="var(--steel-mid)"/>
          <stop offset="1" stop-color="var(--steel-dark)"/>
        </linearGradient>
      </defs>
      <polygon fill="url(#steel)" points="0,1200 0,1010 50,1010 50,1000 70,1000 70,918 110,918 110,985 130,985 130,990 150,990 150,968 185,968 185,995 225,995 225,962 245,962 245,876 285,876 285,948 305,948 305,950 345,950 345,756 395,756 395,810 430,810 430,960 455,960 455,965 480,965 480,960 505,960 505,985 520,985 520,990 545,990 545,846 590,846 590,990 610,990 610,930 650,930 650,990 665,990 665,960 700,960 700,1005 720,1005 720,1030 760,1030 760,948 795,948 795,1010 810,1010 810,1200"/>
    </svg>
  </main>
</body>
</html>
```